Indoor Gun Range Web Design Project

Create a professional bold indoor gun range website. Logo colors are white, red, and black. This is a very professional gun range. Please use high quality stock images if possible. Stay away from a lot of militia type photos. Use your best judgement on what to put as a main image and headline.

Here are some websites that I like for design.

http://www.pinebrookarsenal.example/
http://www.layoutbazaar.example/website-templates/51947.html
http://www.marigoldworks.example/

Target Market(s)

Men ages 25-65

Industry/Entity Type

Gun

Requirements
Must have
• Bold lettering, logo attached, exciting photos.
Should not have
• A lot of militia photos.

```html
<!DOCTYPE html>
<html lang="en">
<head>
<meta charset="utf-8">
<title>Trueline Indoor Gun Range</title>
<link href="https://fonts.googleapis.com/css2?family=Archivo+Black&family=Arimo:wght@400;700&display=swap" rel="stylesheet">
<style>
  :root {
    --red: #d6121b;
    --red-dark: #a70b12;
    --red-deep: #8e070d;
    --ink: #111111;
    --paper: #ffffff;
    --grey-band: #4a4d52;
    --grey-band-light: #6b6e73;
    --footer: #1d1e20;
    --footer-line: #2f3033;
    --footer-text: #8a8c90;
    --gold-top: #ffd34a;
    --gold-bottom: #f2a60c;
    --pill: #e4e4e4;
  }
  * { box-sizing: border-box; margin: 0; padding: 0; }
  html, body { width: 980px; height: 1200px; overflow: hidden; }
  body {
    position: relative;
    font-family: "Arimo", Arial, sans-serif;
    background: var(--paper);
    color: var(--ink);
  }

  /* top navigation */
  .top-nav {
    position: absolute; left: 0; top: 0; width: 980px; height: 42px;
    background: linear-gradient(#e3222a, var(--red-dark));
    border-bottom: 2px solid var(--red-deep);
  }
  .top-nav .menu { position: absolute; left: 98px; top: 0; display: flex; height: 42px; }
  .top-nav .menu a {
    display: block; padding: 0 10px; line-height: 42px;
    color: var(--paper); font-weight: 700; font-size: 14.5px; text-decoration: none;
  }
  .top-nav .menu a:first-child { padding-left: 0; }
  .top-nav .menu a.active { background: var(--red-deep); padding: 0 11px; }
  .top-nav .account { position: absolute; left: 757px; top: 0; display: flex; gap: 28px; }
  .top-nav .account a {
    color: #ffd9da; font-size: 11.5px; line-height: 42px; text-decoration: none;
    display: flex; align-items: center; gap: 5px;
  }

  /* header */
  .site-header { position: absolute; left: 0; top: 44px; width: 980px; height: 100px;
    background: linear-gradient(#fafafa, #ffffff); }
  .brand { position: absolute; left: 95px; top: 38px; }
  .brand-name { font-size: 24px; font-weight: 700; color: var(--red); line-height: 1; white-space: nowrap; }
  .social { position: absolute; left: 805px; top: 34px; display: flex; gap: 6px; }
  .social span { width: 36px; height: 36px; border-radius: 50%; background: #3a3a3a; display: block; }

  /* hero */
  .hero { position: absolute; left: 98px; top: 147px; width: 784px; height: 346px; overflow: hidden;
    background: linear-gradient(180deg, #d2d0cc 0%, #ece9e4 40%, #bdb9b2 100%); }
  .hero-photo { position: absolute; left: 0; top: 0; width: 322px; height: 346px;
    background: linear-gradient(180deg, #9a958c 0%, #b7b1a6 45%, #8a847a 100%); }
  .hero-copy { position: absolute; left: 353px; top: 112px; width: 420px; }
  .hero-title { font-family: "Archivo Black", "Arial Black", sans-serif; font-size: 33px; line-height: 1;
    color: var(--ink); letter-spacing: 0.5px; font-weight: 400; }
  .hero-title em { font-style: normal; color: var(--red); font-size: 42px; }
  .hero-text { margin-top: 8px; font-size: 14.5px; line-height: 17px; color: var(--ink); }
  .btn-join { display: inline-block; margin-top: 15px; width: 203px; height: 38px; line-height: 36px;
    text-align: center; font-family: "Archivo Black", "Arial Black", sans-serif; font-size: 17px; color: #3a2400;
    background: linear-gradient(var(--gold-top), var(--gold-bottom)); border: 1px solid #c9860a; border-radius: 4px;
    text-decoration: none; }
  .slider-arrow { position: absolute; top: 296px; }

  /* feature band */
  .feature-band { position: absolute; left: 0; top: 497px; width: 980px; height: 385px;
    background: radial-gradient(ellipse at 50% 45%, var(--grey-band-light), var(--grey-band) 70%); }
  .feature-band::before { content: ""; position: absolute; left: 0; top: 0; width: 980px; height: 4px;
    background: repeating-linear-gradient(90deg, #ffffff 0 4px, transparent 4px 8px); }
  .card { position: absolute; top: 34px; width: 186px; height: 305px; background: var(--paper);
    border-bottom: 4px solid var(--red); overflow: hidden; }
  .card-title { height: 42px; padding-left: 16px; line-height: 44px; font-size: 16.5px; font-weight: 700; color: var(--red); }
  .card.news .card-title { background: var(--ink); color: var(--paper); }
  .card-media { width: 186px; }
  .btn-more { position: absolute; left: 28px; bottom: 10px; height: 20px; padding: 0 8px 0 10px;
    border-radius: 10px; background: var(--pill); font-size: 10px; line-height: 20px; color: #333;
    display: flex; align-items: center; gap: 6px; text-decoration: none; }
  .btn-more i { width: 10px; height: 10px; border-radius: 50%; background: var(--red); display: block; position: relative; }
  .btn-more i::after { content: ""; position: absolute; left: 3px; top: 2.5px; border-left: 5px solid #fff;
    border-top: 2.5px solid transparent; border-bottom: 2.5px solid transparent; }
  .checks { list-style: none; padding: 12px 14px 0 28px; }
  .checks li { position: relative; font-size: 9.5px; line-height: 11px; color: #333; margin-bottom: 12px; }
  .checks li svg { position: absolute; left: -20px; top: 0; }
  .overlay-note { position: absolute; left: 0; top: 179px; width: 186px; height: 68px; padding: 10px 12px;
    background: rgba(20, 20, 20, 0.78); color: #f0f0f0; font-size: 12.5px; line-height: 14.5px; }
  .review { padding: 14px 18px 0 16px; font-size: 9.5px; line-height: 11.5px; color: #333; }
  .review strong { display: block; margin-top: 10px; font-size: 9.5px; }
  .news-item { position: relative; height: 62px; border-bottom: 1px solid #e2e2e2; padding: 14px 8px 0 34px; }
  .news-date { position: absolute; left: 0; top: 14px; width: 26px; text-align: center; }
  .news-date b { display: block; background: #3a3c40; color: #fff; font-size: 14px; line-height: 22px; }
  .news-date small { display: block; font-size: 9px; color: #999; margin-top: 3px; }
  .news-item h4 { font-size: 11px; line-height: 12px; color: #222; }
  .news-item p { font-size: 9.5px; line-height: 11px; color: #444; margin-top: 2px; }

  /* footer */
  .site-footer { position: absolute; left: 0; top: 882px; width: 980px; height: 318px; background: var(--footer); }
  .footer-heading { position: absolute; top: 41px; display: flex; align-items: center; gap: 9px;
    color: var(--red); font-size: 14px; font-weight: 400; }
  .footer-heading i { width: 12px; height: 12px; border-radius: 50%; background: var(--red); display: block; }
  .link-col { position: absolute; list-style: none; }
  .link-col li { font-size: 10px; line-height: 14px; color: var(--footer-text); padding-left: 13px; position: relative; }
  .link-col li::before { content: ""; position: absolute; left: 0; top: 5px; width: 4px; height: 4px; border-radius: 50%; background: #666; }
  .link-col li.gap { margin-top: 11px; }
  .link-col li.hot { color: var(--red); }
  .subscribe-note { position: absolute; left: 426px; top: 72px; font-size: 10px; color: #bbb; }
  .subscribe-field { position: absolute; left: 426px; top: 90px; width: 189px; height: 20px; background: #fff; border-radius: 3px; }
  .btn-subscribe { position: absolute; left: 426px; top: 116px; height: 18px; padding: 0 10px; border-radius: 9px;
    background: var(--pill); color: var(--red); font-size: 10px; line-height: 18px; }
  .share-bar { position: absolute; left: 428px; top: 152px; width: 187px; height: 31px; background: #fff;
    border-radius: 3px; display: flex; align-items: center; gap: 5px; padding-left: 12px; }
  .share-bar .chip { width: 42px; height: 16px; border: 1px solid #bcc6d6; border-radius: 3px; background: #eef2f8; }
  .share-bar .count { font-size: 9px; color: #555; border: 1px solid #ccc; padding: 1px 4px; border-radius: 2px; }
  .footer-brand { position: absolute; left: 672px; top: 60px; }
  .footer-brand .brand-name { font-size: 14px; color: #3c3d40; }
  .footer-rule { position: absolute; left: 0; top: 213px; width: 980px; height: 1px; background: var(--footer-line); }
  .legal { position: absolute; left: 98px; top: 233px; font-size: 9.5px; line-height: 14px; color: var(--footer-text); }
  .credit { position: absolute; left: 739px; top: 236px; width: 143px; height: 21px; border-radius: 10px;
    background: #2a2b2e; color: var(--footer-text); font-size: 9.5px; line-height: 21px; text-align: center; }
</style>
</head>
<body>

<nav class="top-nav">
  <div class="menu">
    <a href="#">HOME</a>
    <a href="#">RANGE FEES</a>
    <a href="#" class="active">RANGE RULES</a>
    <a href="#">RANGE NEWS</a>
    <a href="#">MEMBERSHIP</a>
    <a href="#">CONTACT</a>
  </div>
  <div class="account">
    <a href="#">Sign In
      <svg width="8" height="9" viewBox="0 0 8 9"><rect x="0.5" y="4" width="7" height="5" fill="#ffd9da"/><path d="M2 4V2.5a2 2 0 0 1 4 0V4" fill="none" stroke="#ffd9da" stroke-width="1.2"/></svg></a>
    <a href="#">Sign Up
      <svg width="8" height="9" viewBox="0 0 8 9"><circle cx="4" cy="2.3" r="2.2" fill="#ffd9da"/><path d="M0 9a4 3.6 0 0 1 8 0z" fill="#ffd9da"/></svg></a>
  </div>
</nav>

<header class="site-header">
  <div class="brand">
    <span class="brand-name">Trueline Indoor Gun Range</span>
  </div>
  <div class="social"><span></span><span></span></div>
</header>

<section class="hero">
  <div class="hero-photo" role="img" aria-label="Shooter in a blue striped shirt and ear protection aiming down an indoor range lane"></div>
  <div class="hero-copy">
    <h1 class="hero-title">INDOOR<em>GUN</em>RANGE!</h1>
    <p class="hero-text">Lorem ipsum dolor sit amet, consectetur adipiscing elit. Praesent elementum dui id. Consectetur adipiscing sed non est eu lectus adipiscing hendrerit.</p>
    <a href="#" class="btn-join">Join Membership!</a>
  </div>
</section>
<svg class="slider-arrow" style="left:66px" width="22" height="40" viewBox="0 0 22 40"><path d="M19 2 3 20l16 18" fill="none" stroke="#c9c9c9" stroke-width="3"/></svg>
<svg class="slider-arrow" style="left:892px" width="22" height="40" viewBox="0 0 22 40"><path d="M3 2l16 18L3 38" fill="none" stroke="#c9c9c9" stroke-width="3"/></svg>

<section class="feature-band">
  <article class="card" style="left:98px">
    <h3 class="card-title">Featured Rules</h3>
    <div class="card-media" role="img" aria-label="Man in a white tank top holding a pistol under a stormy sky" style="height:151px;background:linear-gradient(#7c8088,#a7a9ac 55%,#5e6063)"></div>
    <ul class="checks">
      <li><svg width="13" height="11" viewBox="0 0 13 11"><path d="M1 6l4 4 7-9" fill="none" stroke="#6aa51d" stroke-width="2.4"/></svg>Lorem ipsum dolor sit amet, conse ctetur adipis cing elit.</li>
      <li><svg width="13" height="11" viewBox="0 0 13 11"><path d="M1 6l4 4 7-9" fill="none" stroke="#6aa51d" stroke-width="2.4"/></svg>Lorem ipsum dolor sit amet, conse ctetur adipis cing elit.</li>
    </ul>
    <a href="#" class="btn-more">Learn More <i></i></a>
  </article>

  <article class="card" style="left:297px">
    <h3 class="card-title">What's Speciality?</h3>
    <div class="card-media" role="img" aria-label="Man in a dark suit holding a handgun" style="height:263px;background:linear-gradient(#9ea2a8,#5c5f64 60%,#2e3033)"></div>
    <p class="overlay-note">Mauris pretium metus eu arcu aliquet sit amet vulput ate eros suscipit.</p>
    <a href="#" class="btn-more" style="left:14px">Learn More <i></i></a>
  </article>

  <article class="card" style="left:496px">
    <h3 class="card-title">Recent Reviews</h3>
    <div class="card-media" role="img" aria-label="Man in a black top aiming a pistol with both hands" style="height:113px;background:linear-gradient(#c9b8a8,#8e7766 60%,#5a4a40)"></div>
    <div class="review">Lorem ipsum dolor sit amet, conse ctetur adipis cing elit.Lorem ipsum dolor sit amet, conse ctetur adipis cing elit.Lorem ipsum dolor sit amet, conse ctetur adipis cing elit.
      <strong>Mark Dalton, UAE</strong></div>
    <a href="#" class="btn-more" style="left:18px">Learn More <i></i></a>
  </article>

  <article class="card news" style="left:696px">
    <h3 class="card-title">News Range</h3>
    <div class="news-item">
      <div class="news-date"><b>12</b><small>Jan</small></div>
      <h4>Lorem ipsum dolor sit ame</h4>
      <p>Vivamus felis augue, facilisis nec, tristique sed nulla.</p>
    </div>
    <div class="news-item">
      <div class="news-date"><b>11</b><small>Jan</small></div>
      <h4>Lorem ipsum dolor sit ame</h4>
      <p>Vivamus felis augue, facilisis nec, tristique sed nulla.</p>
    </div>
    <div class="news-item" style="border:0">
      <div class="news-date"><b>10</b><small>Jan</small></div>
      <h4>Lorem ipsum dolor sit ame</h4>
      <p>Lorem ipsum dolor sit amet, conse ctetur adipis cing elit.Lorem ipsum dolor sit amet, conse ctetur adipis cing</p>
    </div>
    <a href="#" class="btn-more" style="left:34px">Learn More <i></i></a>
  </article>
</section>

<footer class="site-footer">
  <h4 class="footer-heading" style="left:94px"><i></i>Trueline Indoor Gun Range Quick Links</h4>
  <ul class="link-col" style="left:97px;top:74px">
    <li>Home</li><li>Why Us?</li><li>Contact Us</li><li>FAQ</li>
    <li class="gap">Live Chat</li><li>Testimonials</li><li>Our Corporate Reviews</li><li>New batch for the Month</li>
  </ul>
  <ul class="link-col" style="left:251px;top:74px">
    <li>Range Fees</li><li>Range Rules</li><li>Range Support</li><li>Locate us</li>
    <li class="gap">Membership</li><li class="hot">Range Corporate Class</li><li>Collaboration &amp; Awards</li><li>News</li>
  </ul>

  <h4 class="footer-heading" style="left:425px"><i></i>Join Our Mail Listing</h4>
  <p class="subscribe-note">Please enter you email address to subscribe</p>
  <div class="subscribe-field"></div>
  <span class="btn-subscribe">Subscribe</span>
  <div class="share-bar">
    <span class="chip"></span><span class="count">1,186</span>
    <span class="chip" style="width:34px"></span><span class="chip" style="width:20px;background:#fff;border-color:#ccc"></span><span class="count" style="border:0;padding:0">19</span>
  </div>

  <div class="footer-brand">
    <span class="brand-name">Trueline Indoor Gun Range</span>
  </div>

  <div class="footer-rule"></div>
  <p class="legal">Copyright - 2012. All right reserved.<br>All brand and product names are trademarks or registered trademarks of their respective companies.</p>
  <p class="credit">Powered By : Kestrel Web Works</p>
</footer>

</body>
</html>
```